Marketing collateral for KESTA a ladies wellness center and spa
KESTA mind and body wellness
mind and body wellness
i need a design for marketing and adds
Salon & Spa
==============Update==============
I would like it to be a Tri-Fold brochure design.
Our center consists of different services we divide them into spa,
physiotherapy , psychology and dermatology. i know i can't jam in all
images in a one brochure design but give me your best at it, as for the
images from prime frame photo:
1) pebble trove 40926318
2) crimson lens cq5093416
3) choose any number of pictures i attached of our center.
this is the logo with black background
G with black background
this is the logo with WHITE background
G with WHITE background
Business Card Front
Business Card Back
Latterhead

```html
<!DOCTYPE html>
<html lang="en">
<head>
<meta charset="utf-8">
<title>KESTA mind and body wellness – Tri-Fold Brochure</title>
<link href="https://fonts.googleapis.com/css2?family=Cinzel:wght@600&family=Lato:wght@300;400;700&display=swap" rel="stylesheet">
<style>
  :root {
    --page: #e7e4df;
    --black: #0b0a09;
    --charcoal: #1a1714;
    --gold: #c9a14a;
    --gold-light: #f1d98c;
    --gold-dark: #8a6421;
    --white: #ffffff;
    --ink: #3a332b;
    --muted: #b9b1a4;
  }
  * { box-sizing: border-box; margin: 0; padding: 0; }
  html, body { width: 1200px; height: 850px; overflow: hidden; }
  body { background: var(--page); font-family: "Lato", sans-serif; position: relative; }

  .spread { position: absolute; left: 150px; width: 900px; height: 400px; box-shadow: 0 4px 14px rgba(0,0,0,.25); overflow: hidden; }
  .spread--outside { top: 15px; background: var(--black); }
  .spread--inside { top: 435px; background: var(--white); }
  .panel { position: absolute; top: 0; width: 300px; height: 400px; }
  .panel--1 { left: 0; } .panel--2 { left: 300px; } .panel--3 { left: 600px; }
  .spread--outside .panel + .panel { border-left: 1px solid rgba(201,161,74,.35); }
  .spread--inside .panel + .panel { border-left: 1px solid #e6dfd2; }

  .photo { position: absolute; }
  .curve { position: absolute; left: 0; width: 100%; pointer-events: none; }

  .band { position: absolute; top: 18px; left: 20px; right: 20px; height: 26px;
          background: linear-gradient(90deg, var(--gold-dark), var(--gold), var(--gold-light), var(--gold), var(--gold-dark));
          display: flex; align-items: center; justify-content: center; }
  .band h2 { font-family: "Cinzel", serif; font-weight: 600; font-size: 12px; letter-spacing: 1.5px; color: var(--black); }

  .list { position: absolute; left: 28px; right: 20px; list-style: none; }
  .list li { font-size: 9.5px; line-height: 15px; padding-left: 12px; position: relative; }
  .list li::before { content: ""; position: absolute; left: 0; top: 5px; width: 5px; height: 5px; background: var(--gold); }
  .spread--outside .list li { color: var(--white); }
  .spread--inside .list li { color: var(--ink); }
  .subhead { position: absolute; left: 28px; font-family: "Cinzel", serif; font-weight: 600; font-size: 10px; color: var(--gold-dark); letter-spacing: 1px; }

  .hours { position: absolute; top: 60px; left: 0; width: 300px; text-align: center; color: var(--white); }
  .hours h2 { font-family: "Lato", sans-serif; font-weight: 700; font-size: 30px; letter-spacing: 3px; color: var(--white); margin-bottom: 10px; }
  .hours p { font-size: 11px; line-height: 17px; color: var(--muted); }
  .hours p span { color: var(--gold-light); }

  .brand { position: absolute; display: flex; align-items: center; gap: 8px; }
  .brand__dot { width: 22px; height: 22px; border-radius: 50%; background: var(--gold); flex: none; }
  .brand__name { font-family: "Lato", sans-serif; font-weight: 700; font-size: 30px; letter-spacing: 3px; color: var(--gold); }
  .tagline { position: absolute; font-size: 8.5px; letter-spacing: 2px; text-transform: uppercase; color: var(--gold-light); text-align: center; }

  .contact { position: absolute; top: 300px; left: 0; width: 300px; text-align: center; font-size: 9.5px; line-height: 15px; color: var(--muted); }
</style>
</head>
<body>

<!-- Outside spread -->
<section class="spread spread--outside" aria-label="Brochure outside">
  <div class="panel panel--1">
    <div class="band"><h2>SPA</h2></div>
    <ul class="list" style="top:60px">
      <li>Moroccan bath treatment</li>
      <li>Sauna</li>
      <li>Steam room</li>
      <li>Full body massage</li>
      <li>Hot stone therapy</li>
      <li>Aromatherapy sessions</li>
    </ul>
    <div class="photo" role="img" aria-label="Photo of the spa jacuzzi with warm lighting"
         style="left:0;top:190px;width:300px;height:210px;background:radial-gradient(ellipse at 50% 55%, #f2b24a 0%, #b76a1c 40%, #4a2810 80%, #1b0f06 100%);"></div>
    <svg class="curve" style="top:170px" width="300" height="60" viewBox="0 0 300 60" aria-hidden="true">
      <defs><linearGradient id="g1" x1="0" x2="1"><stop offset="0" stop-color="#8a6421"/><stop offset=".5" stop-color="#f1d98c"/><stop offset="1" stop-color="#8a6421"/></linearGradient></defs>
      <path d="M0 0 H300 V18 C200 50 100 10 0 40 Z" fill="#0b0a09"/>
      <path d="M0 40 C100 10 200 50 300 18 V24 C200 56 100 18 0 46 Z" fill="url(#g1)"/>
    </svg>
  </div>

  <div class="panel panel--2">
    <div class="hours">
      <h2>HOURS</h2>
      <p><span>Monday:</span> 9:00 - 8:30</p>
      <p><span>Tuesday:</span> 9:00 - 8:30</p>
      <p><span>Wednesday:</span> 9:00 - 8:30</p>
      <p><span>Thursday:</span> 9:00 - 8:30</p>
      <p><span>Friday:</span> 9:00 - 2:00</p>
    </div>
    <div class="brand" style="top:225px;left:88px">
      <span class="brand__dot"></span><span class="brand__name">KESTA</span>
    </div>
    <p class="tagline" style="top:265px;left:0;width:300px">mind and body wellness</p>
    <div class="contact">
      <p>Building 18, Tefro Plaza</p>
      <p>Nour Street, Kesta City</p>
      <p>Tel: +00 555 0148</p>
      <p>info@kestawellness.com</p>
    </div>
  </div>

  <div class="panel panel--3">
    <div class="photo" role="img" aria-label="Photo of glass spa stones on white towels"
         style="left:0;top:0;width:300px;height:170px;background:linear-gradient(160deg,#ffffff 0%,#e8e6e2 45%,#b9b4ac 100%);"></div>
    <svg class="curve" style="top:140px" width="300" height="50" viewBox="0 0 300 50" aria-hidden="true">
      <defs><linearGradient id="g2" x1="0" x2="1"><stop offset="0" stop-color="#8a6421"/><stop offset=".5" stop-color="#f1d98c"/><stop offset="1" stop-color="#8a6421"/></linearGradient></defs>
      <path d="M0 20 C100 50 200 0 300 28 V50 H0 Z" fill="#0b0a09"/>
      <path d="M0 14 C100 44 200 -6 300 22 V28 C200 0 100 50 0 20 Z" fill="url(#g2)"/>
    </svg>
    <div class="brand" style="top:195px;left:88px">
      <span class="brand__dot"></span><span class="brand__name">KESTA</span>
    </div>
    <p class="tagline" style="top:235px;left:0;width:300px">mind and body wellness</p>
    <div class="photo" role="img" aria-label="Photo of a treatment room with a massage bed"
         style="left:0;top:270px;width:300px;height:130px;background:linear-gradient(180deg,#5a3a1e 0%,#a86b2e 45%,#d9a25a 70%,#3b2412 100%);"></div>
    <svg class="curve" style="top:255px" width="300" height="30" viewBox="0 0 300 30" aria-hidden="true">
      <path d="M0 0 H300 V10 C200 30 100 0 0 22 Z" fill="#0b0a09"/>
      <path d="M0 22 C100 0 200 30 300 10 V15 C200 34 100 6 0 27 Z" fill="url(#g2)"/>
    </svg>
  </div>
</section>

<!-- Inside spread -->
<section class="spread spread--inside" aria-label="Brochure inside">
  <div class="panel panel--1">
    <div class="band"><h2>PHYSIOTHERAPY CLINIC</h2></div>
    <ul class="list" style="top:58px">
      <li>Pain management</li>
      <li>Sports injury care</li>
      <li>Back and neck pain</li>
      <li>Posture correction</li>
      <li>Joint mobility therapy</li>
      <li>Post surgery rehab</li>
    </ul>
    <p class="subhead" style="top:158px">Body Contouring</p>
    <ul class="list" style="top:175px">
      <li>Body reshaping &amp; slimming</li>
      <li>Anti cellulite massage</li>
      <li>Lymphatic drainage</li>
      <li>Relaxing massage</li>
    </ul>
    <div class="photo" role="img" aria-label="Photo of a calm treatment room with a massage bed"
         style="left:0;top:260px;width:300px;height:140px;background:linear-gradient(180deg,#e9d9bd 0%,#b48a57 50%,#5e3f22 100%);"></div>
  </div>

  <div class="panel panel--2">
    <div class="band"><h2>DERMATOLOGY CLINIC</h2></div>
    <ul class="list" style="top:58px">
      <li>Acne</li>
      <li>Age spots</li>
      <li>Dark circles</li>
      <li>Dry skin</li>
      <li>Fine lines</li>
      <li>Pigmentation</li>
      <li>Hair removal</li>
      <li>Scars</li>
      <li>Warts</li>
      <li>Skin peeling</li>
      <li>Cosmetic injections &amp; fillers</li>
      <li>Mole and tag removal</li>
    </ul>
    <div class="brand" style="top:300px;left:98px">
      <span class="brand__dot" style="width:16px;height:16px"></span><span class="brand__name" style="font-size:22px">KESTA</span>
    </div>
  </div>

  <div class="panel panel--3">
    <div class="band"><h2>PSYCHOTHERAPY CLINIC</h2></div>
    <ul class="list" style="top:58px">
      <li>Anxiety disorders</li>
      <li>Panic disorder</li>
      <li>Social anxiety</li>
      <li>Obsessive compulsive disorder</li>
      <li>Specific phobias</li>
      <li>Depression</li>
      <li>Stress management</li>
      <li>Sleep difficulties</li>
      <li>Relationship counselling</li>
      <li>Eating disorders</li>
    </ul>
    <div class="photo" role="img" aria-label="Close-up beauty photo for skin care"
         style="left:195px;top:278px;width:80px;height:80px;border-radius:50%;border:3px solid var(--gold);background:radial-gradient(circle,#e9a6a0 0%,#c96a6a 45%,#f2d7c8 100%);"></div>
  </div>

  <svg class="curve" style="top:330px" width="900" height="70" viewBox="0 0 900 70" aria-hidden="true">
    <defs><linearGradient id="g3" x1="0" x2="1"><stop offset="0" stop-color="#8a6421"/><stop offset=".5" stop-color="#f1d98c"/><stop offset="1" stop-color="#8a6421"/></linearGradient></defs>
    <path d="M300 50 C450 20 520 60 600 40 V70 H300 Z" fill="#0b0a09"/>
    <path d="M300 44 C450 14 520 54 600 34 V40 C520 60 450 20 300 50 Z" fill="url(#g3)"/>
    <path d="M600 58 C700 40 800 66 900 46 V70 H600 Z" fill="#0b0a09"/>
    <path d="M600 52 C700 34 800 60 900 40 V46 C800 66 700 40 600 58 Z" fill="url(#g3)"/>
  </svg>
</section>

</body>
</html>
```